OV Holdings Invitation

I need an invitation designed for both online and hard copy distribution. I'm uploading a poorly designed online invitation that includes our logo and the blue and black colors we want to use. The online invitation must have an area to embed video (see attached).

With regard to the hard copy invitation, we need it to be a 5x7 card. Where the embedded video is on the online version, we would like you to create an image that represents the terms "monetizing innovation". If you go to www.ovhold.co, you can see what the company is using to express those words right now. There are no limitations to what you come up with for this visual.

Please note: The invitation both online and hardcopy must be designed so that all the information in the attached copy can be read. This includes: Logo, hosted by; When/date, where, two quotes, etc.

I've attached our logo files. You can use whichever logo file you want for your design.

Many thanks...looking forward to seeing all your great designs.
Updates

All - you do not need to follow our format for the invite as long as all the information we need is on it....Note:  we will need to be able to edit the information for other presentation.

EPS files of the logo have been added for those of you who have requested it.

Many thanks,

Marta

Reason: All, Apologies for the extension. The decision-makers have been travelling and have not had a chance to thoroughly review the designs. We really appreciate your patience. Many thanks, Marta

Target Market(s)

Investors and Media

Industry/Entity Type

It Company

Requirements
Must have
• Please use the blue and black colors as seen in the attached uploaded files.

```html
<!DOCTYPE html>
<html lang="en">
<head>
<meta charset="utf-8">
<title>OV Holdings Invitation</title>
<link rel="stylesheet" href="https://fonts.googleapis.com/css2?family=Roboto+Condensed:wght@400;700&family=Libre+Baskerville:wght@700&display=swap">
<style>
  :root {
    --blue: #1a5aa6;
    --blue-dark: #164a8c;
    --ink: #1d1d1d;
    --paper: #ffffff;
    --grey: #e6e6e8;
    --grey-light: #efeff1;
    --border: #5b82b8;
    --ornament: #d3e1f2;
  }
  * { margin: 0; padding: 0; box-sizing: border-box; }
  html, body { width: 1200px; height: 858px; overflow: hidden; background: var(--paper); }
  body { font-family: "Roboto Condensed", "Arial Narrow", sans-serif; color: var(--ink); }
  .invitation {
    position: relative; width: 1200px; height: 858px;
    border: 1px solid var(--border); overflow: hidden; background: var(--paper);
  }
  .decor { position: absolute; inset: 0; }
  .ornament {
    position: absolute; left: 552px; width: 96px; height: 14px;
    border-radius: 7px; background: var(--ornament);
  }
  .ornament--top { top: 23px; }
  .ornament--mid { top: 226px; }
  .quotes { position: absolute; top: 59px; left: 0; width: 1200px; text-align: center; }
  .quote { font-size: 17px; line-height: 26px; color: var(--blue); }
  .quote strong { font-weight: 700; }
  .source {
    font-family: "Libre Baskerville", Georgia, serif; font-weight: 700;
    font-size: 22px; line-height: 30px; color: var(--ink); letter-spacing: 0.5px; margin: 0 0 12px;
  }
  .source--second { font-size: 21px; margin: 0; }
  .special {
    position: absolute; left: 36px; top: 222px;
    font-size: 20px; font-weight: 700; color: var(--blue);
  }
  .brand {
    position: absolute; left: 96px; top: 332px;
    display: flex; align-items: center; gap: 12px;
    font-size: 30px; font-weight: 700; color: var(--ink); letter-spacing: 2px;
  }
  .brand__mark { width: 26px; height: 26px; background: var(--blue); }
  .video {
    position: absolute; left: 421px; top: 288px; width: 358px; height: 270px;
    background: #101216;
  }
  .video__screen {
    position: absolute; left: 4px; top: 4px; width: 350px; height: 228px;
    background: radial-gradient(circle at 80% 30%, #e8d79a 0%, #8c8fc8 30%, #3c4fb0 65%, #1f2e86 100%);
  }
  .video__play { position: absolute; left: 10px; top: 238px; width: 26px; height: 26px; }
  .details {
    position: absolute; top: 602px; left: 192px;
    display: flex; font-size: 16.5px; line-height: 23px;
  }
  .details__col { padding-right: 20px; }
  .details__col--hosts { width: 230px; }
  .details__col--where { width: 326px; padding-left: 63px; border-left: 3px solid var(--blue); height: 84px; }
  .details__col--when { padding-left: 59px; border-left: 3px solid var(--blue); height: 84px; }
  .details h3 { font-size: 16.5px; font-weight: 700; color: var(--blue-dark); }
  .rsvp {
    position: absolute; left: 737px; top: 736px;
    font-size: 16.5px; line-height: 25px; color: var(--blue);
  }
  .rsvp__note { font-size: 12px; line-height: 18px; color: var(--ink); margin-top: 4px; }
</style>
</head>
<body>
<main class="invitation">
  <svg class="decor" width="1200" height="858" viewBox="0 0 1200 858" aria-hidden="true">
    <polygon points="1042,0 1200,0 1200,518 1042,628" fill="var(--grey)"/>
    <polygon points="1200,560 1200,640 1020,858 940,858" fill="var(--grey-light)"/>
    <polygon points="0,800 40,756 150,756 70,858 0,858" fill="var(--grey-light)"/>
    <polygon points="150,858 230,756 340,756 260,858" fill="var(--grey-light)"/>
    <polygon points="340,858 420,756 530,756 450,858" fill="var(--grey-light)"/>
    <polygon points="530,858 610,756 700,756 620,858" fill="var(--grey-light)"/>
  </svg>

  <div class="ornament ornament--top" role="img" aria-label="Decorative flourish"></div>

  <section class="quotes">
    <p class="quote"><strong>In the biggest breakthrough against malaria in years,</strong> scientist yesterday said<br>they had identified the odor molecules that baffle blood-thirsty mosquitoes</p>
    <p class="source">THE SOUTHERN HERALD</p>
    <p class="quote"><strong>Confusing mosquitoes to fight deadly disease</strong></p>
    <p class="source source--second">Pacific Coast Journal</p>
  </section>

  <div class="ornament ornament--mid" role="img" aria-label="Decorative flourish"></div>

  <p class="special">A special presentation of</p>
  <div class="brand"><span class="brand__mark"></span>OV Holdings</div>

  <div class="video">
    <div class="video__screen" role="img" aria-label="Embedded news video about the malaria research"></div>
    <svg class="video__play" viewBox="0 0 26 26" aria-hidden="true">
      <rect x="1" y="1" width="24" height="24" rx="4" fill="#2a2a2a" stroke="#888"/>
      <polygon points="9,7 19,13 9,19" fill="#ddd"/>
    </svg>
  </div>

  <section class="details">
    <div class="details__col details__col--hosts">
      <h3>Hosted By:</h3>
      <p>Rami Haddad, CEO<br>Glen Porter, President<br>Luis Moreno, CFO<br>Mark Ellison, COO<br>Owen Blake, CCO</p>
    </div>
    <div class="details__col details__col--where">
      <h3>Where:</h3>
      <p>Harbor Crest Inn - Bayview Room<br>1820 Crestview Ave<br>Lakemont CA 92415</p>
    </div>
    <div class="details__col details__col--when">
      <h3>When:</h3>
      <p>Wednesday, September 28th<br>Check-In 3:00 pm<br>Presentation 3:30-4:30 pm</p>
    </div>
  </section>

  <section class="rsvp">
    <p>Please RSVP by Monday, September 26th</p>
    <p>Nora Whitfield</p>
    <p>(877) 555-0148 x 1003 nwhitfield@ovhold.co</p>
    <p class="rsvp__note">*Please note that you must be an accredited investor to attend the presentation</p>
  </section>
</main>
</body>
</html>
```